Sleek, Professional Business Card Design Needed

Business Cards - Logo Attached.

We are a solar consulting company. We are national and want our cards to represent the professional high quality products that we offer.

Industry/Entity Type

Business

Contact Information for Business Card

n/a

Requirements
Must have
• Design
• Name
• Position
• Number
• Email
• Address
Should not have
• Not be too crowded

```html
<!DOCTYPE html>
<html lang="en">
<head>
<meta charset="utf-8">
<title>Brightfield Solar – Business Card</title>
<link href="https://fonts.googleapis.com/css2?family=Lato:wght@400;700&display=swap" rel="stylesheet">
<style>
  :root {
    --brand-blue: #1b8fd3;
    --brand-green: #7cba2f;
    --ink: #4a4a4a;
    --card: #f7f8f7;
    --stage: #e4e6e8;
    --wash-blue: rgba(27, 143, 211, 0.10);
    --wash-green: rgba(124, 186, 47, 0.10);
  }
  * { box-sizing: border-box; margin: 0; padding: 0; }
  html, body {
    width: 1200px; height: 786px; overflow: hidden;
    background: var(--stage);
    font-family: "Lato", Arial, sans-serif;
  }
  .stage {
    position: relative; width: 1200px; height: 786px;
    display: flex; align-items: center; justify-content: center; gap: 50px;
  }
  .card {
    position: relative; width: 525px; height: 300px;
    background: var(--card);
    box-shadow: 0 6px 18px rgba(0,0,0,0.18);
    overflow: hidden;
  }
  .brand-mark {
    display: flex; align-items: center; gap: 10px;
  }
  .brand-dot {
    width: 34px; height: 34px; border-radius: 50%;
    border: 4px solid var(--brand-blue);
  }
  .brand-name {
    font-weight: 700; color: var(--brand-green);
    font-size: 26px; letter-spacing: 1px; text-transform: uppercase;
  }
  .decor-wash {
    position: absolute; border-radius: 50%;
    background: radial-gradient(circle, var(--wash-green) 0%, var(--wash-blue) 60%, transparent 72%);
  }
  /* front */
  .card--front .decor-wash { width: 420px; height: 420px; left: 52px; top: -60px; }
  .card--front .brand-mark {
    position: absolute; left: 50%; top: 50%; transform: translate(-50%, -50%);
  }
  /* back */
  .card--back .brand-mark { position: absolute; left: 40px; top: 48px; }
  .card--back .brand-name { font-size: 22px; }
  .card--back .brand-dot { width: 30px; height: 30px; }
  .contact {
    position: absolute; left: 268px; top: 130px;
    color: var(--ink); font-size: 13px; line-height: 1.55;
  }
  .contact__name {
    font-size: 21px; letter-spacing: 1px; text-transform: uppercase; line-height: 1.1;
  }
  .contact__first { color: var(--brand-blue); }
  .contact__last { color: var(--brand-green); }
  .contact__role { margin-bottom: 10px; }
  .contact__line { display: flex; align-items: center; gap: 7px; }
  .contact__line svg { width: 12px; height: 12px; fill: var(--brand-blue); flex: none; }
</style>
</head>
<body>
<main class="stage">
  <section class="card card--front" aria-label="Card front">
    <div class="decor-wash" role="img" aria-label="Faint oversized brand emblem watermark"></div>
    <div class="brand-mark">
      <span class="brand-dot"></span>
      <span class="brand-name">Brightfield Solar</span>
    </div>
  </section>

  <section class="card card--back" aria-label="Card back">
    <div class="brand-mark">
      <span class="brand-dot"></span>
      <span class="brand-name">Brightfield Solar</span>
    </div>
    <div class="contact">
      <p class="contact__name"><span class="contact__first">Marcus</span> <span class="contact__last">Ellery</span></p>
      <p class="contact__role">Managing Director</p>
      <p>Orchard Lane, 8/B</p>
      <p>Ludlow, SY8 2PT</p>
      <p class="contact__line">
        <svg viewBox="0 0 24 24" aria-hidden="true"><path d="M6.6 10.8a15.1 15.1 0 0 0 6.6 6.6l2.2-2.2c.3-.3.7-.4 1-.2 1.1.4 2.3.6 3.6.6.6 0 1 .4 1 1V20c0 .6-.4 1-1 1A17 17 0 0 1 3 4c0-.6.4-1 1-1h3.5c.6 0 1 .4 1 1 0 1.3.2 2.5.6 3.6.1.3 0 .7-.2 1z"/></svg>
        +1-202-555-0187
      </p>
      <p class="contact__line">
        <svg viewBox="0 0 24 24" aria-hidden="true"><path d="M2 5h20v14H2zm2 2v.5l8 5 8-5V7l-8 5z"/></svg>
        hello@brightfieldsolar.com
      </p>
    </div>
  </section>
</main>
</body>
</html>
```